Design a Postcard app mockup

When travelling user can take a picture, add his own greeting-text and send it as a real postcard right from his mobile device. The postcard will be printed by us and delivered directly to the recipients door.
Surprise your friends with your own postcard even during your vacation or use postcards for invitations to wedding, birthdays or other parties!
Unforgettable moments - easy to capture and share.

This app design will be used in both - iOS and Android, so please keep that in mind that it has to work on phones and tablets for iOS and Android.
We need each screen for a tablet (10 inch) and phone (4.7 inch)

Please see the attached wireframes we have developed:

Step 1: Splash screens; - 3 screens (please see in the attached wireframes the screens we would like you to make - they're with a red outline)
(info about the app);

Step 2: Postcard order process: - 7 screens (please see in the attached wireframes the screens we would like you to make - they're with a red outline)
1. Make or select 1 Photo;
2. Add customized text;
3. Select a recipient;
4. Payment process;

Step 3: Projects menu; - 1 screen (please see in the attached wireframes the screens we would like you to make - they're with a red outline)
(see your unfinished postcards)

Step 4: Main menu: - 1 screen (please see in the attached wireframes the screens we would like you to make - they're with a red outline)
1. about;
2. settings;
3. support;
4. contacts;
5. privacy policy

The Logo of the app will be placed by us in the final version. Until then please keep in mind that the background color for the logo is #CC071E and the logo font color will be #6D6E71. The design of the app must be clean, modern looking and all icons should be easy to understand.

```html
<!DOCTYPE html>
<html lang="en">
<head>
<meta charset="utf-8">
<title>Home – Postcard</title>
<link rel="stylesheet" href="https://fonts.googleapis.com/css2?family=PT+Sans:wght@400;700&family=Raleway:wght@200;300&display=swap">
<style>
  :root {
    --brand-red: #cc0a1f;
    --tab-red: #cf091f;
    --tab-inactive: #9a0414;
    --divider-red: #e0374a;
    --tile-camera: #dc1029;
    --tile-gallery: #e8132b;
    --tile-lumo: #ee0a25;
    --tile-circlo: #dd0720;
    --white: #ffffff;
    --rule-grey: #c9c9c9;
  }
  * { margin: 0; padding: 0; box-sizing: border-box; }
  html, body { width: 676px; height: 1200px; overflow: hidden; background: var(--white); }
  body { font-family: "PT Sans", Arial, sans-serif; position: relative; }

  .app-bar {
    position: absolute; left: 0; top: 0; width: 676px; height: 83px;
    background: var(--brand-red);
    border-bottom: 1px solid var(--divider-red);
  }
  .menu-button { position: absolute; left: 32px; top: 27px; width: 36px; height: 30px; }
  .menu-button span {
    position: absolute; left: 0; width: 36px; height: 5px; border-radius: 3px; background: var(--white);
  }
  .menu-button span:nth-child(1) { top: 2px; }
  .menu-button span:nth-child(2) { top: 12px; }
  .menu-button span:nth-child(3) { top: 22px; }
  .screen-title {
    position: absolute; left: 0; right: 0; top: 18px; text-align: center;
    font-family: "Raleway", Arial, sans-serif; font-weight: 300; font-size: 38px;
    letter-spacing: 1px; color: var(--white);
  }

  .tab-bar {
    position: absolute; left: 0; top: 83px; width: 676px; height: 81px;
    background: var(--tab-red);
  }
  .tab {
    position: absolute; top: 0; width: 338px; height: 81px;
    text-align: center; line-height: 76px; font-size: 27px;
  }
  .tab-postcard { left: 0; color: var(--white); }
  .tab-project { left: 338px; color: var(--tab-inactive); }
  .tab-indicator {
    position: absolute; left: 42px; top: 78px; width: 255px; height: 4px; background: var(--white);
  }
  .tab-divider {
    position: absolute; left: 337px; top: 5px; width: 1px; height: 72px; background: var(--divider-red);
  }

  .source-grid { position: absolute; left: 0; top: 164px; width: 676px; height: 422px; }
  .source-tile {
    position: absolute; width: 338px; height: 211px; color: var(--white);
  }
  .source-tile svg { position: absolute; }
  .source-label {
    position: absolute; font-size: 22px; line-height: 33px; white-space: nowrap;
  }
  .tile-camera { left: 0; top: 0; background: var(--tile-camera); }
  .tile-gallery { left: 338px; top: 0; background: var(--tile-gallery); }
  .tile-lumo { left: 0; top: 211px; background: var(--tile-lumo); }
  .tile-circlo { left: 338px; top: 211px; background: var(--tile-circlo); }

  .project-list { position: absolute; left: 39px; top: 586px; width: 597px; list-style: none; }
  .project-row { height: 73px; border-bottom: 2px solid var(--rule-grey); }
  .project-row:first-child { height: 90px; }
</style>
</head>
<body>
  <header class="app-bar">
    <div class="menu-button" aria-label="Menu"><span></span><span></span><span></span></div>
    <h1 class="screen-title">HOME</h1>
  </header>

  <nav class="tab-bar">
    <div class="tab tab-postcard">POSTCARD</div>
    <div class="tab tab-project">PROJECT</div>
    <div class="tab-indicator"></div>
    <div class="tab-divider"></div>
  </nav>

  <section class="source-grid">
    <div class="source-tile tile-camera">
      <svg style="left:37px;top:62px" width="90" height="78" viewBox="0 0 90 78" fill="none" stroke="#fff" stroke-width="6" stroke-linejoin="round">
        <path d="M4 20 H26 L34 4 H62 L70 20 H86 V74 H4 Z"/>
        <circle cx="45" cy="45" r="16"/>
      </svg>
      <div class="source-label" style="left:146px;top:66px">Take a new<br>picture</div>
    </div>

    <div class="source-tile tile-gallery">
      <svg style="left:37px;top:62px" width="80" height="64" viewBox="0 0 80 64" fill="none" stroke="#fff" stroke-width="6" stroke-linejoin="round">
        <rect x="3" y="3" width="74" height="58"/>
        <path d="M12 52 L30 32 L46 48 L56 40 L68 52"/>
        <circle cx="60" cy="17" r="5" fill="#fff" stroke="none"/>
      </svg>
      <div class="source-label" style="left:134px;top:66px">Select from<br>Gallery</div>
    </div>

    <div class="source-tile tile-lumo">
      <svg style="left:47px;top:74px" width="68" height="68" viewBox="0 0 68 68" fill="none" stroke="#fff" stroke-width="6">
        <rect x="3" y="3" width="62" height="62" rx="6"/>
      </svg>
      <div class="source-label" style="left:145px;top:70px">Get your<br>Lumo picture</div>
    </div>

    <div class="source-tile tile-circlo">
      <svg style="left:36px;top:60px" width="80" height="80" viewBox="0 0 80 80" fill="none" stroke="#fff" stroke-width="5">
        <circle cx="40" cy="40" r="37"/>
      </svg>
      <div class="source-label" style="left:134px;top:75px">Get your<br>Circlo picture</div>
    </div>
  </section>

  <ul class="project-list">
    <li class="project-row"></li>
    <li class="project-row"></li>
    <li class="project-row"></li>
    <li class="project-row"></li>
    <li class="project-row"></li>
    <li class="project-row"></li>
    <li class="project-row"></li>
  </ul>
</body>
</html>
```